Tranquil Pathway Business Card

Logo attached. (will be printing onto thick white/off white textured card)

Double sided business card for two Therapists working at Tranquil Pathway.

Require one design, but with different name and mobile numbers on each card.

Target Market(s)

Medical, Health

Industry/Entity Type

Business

Contact Information for Business Card

Need one business card design, but a separate card for each person - Colin Marchetti and Marieke de Boeckx.

FRONT OF CARD

Logo

Name (Colin Marchetti on one card, Marieke de Boeckx on the other)
Professional Clinical Hypnotherapist

Consulting Rooms (Near Lindqvist Hospital)
482 Brackenfield Road
Dunmore VIC 3987

Colin@TranquilPathway.example.au OR Marieke@TranquilPathway.example.au

Mobile: 0455 872 604 (for Colin) OR
Mobile: 0467 290 518 (for Marieke)

BACK OF CARD

Logo

Website: www.TranquilPathway.example.au

Phone: 1300 958 471

Requirements
Must have
• Text and logo only. No additiional graphics.

```html
<!DOCTYPE html>
<html lang="en">
<head>
<meta charset="utf-8">
<title>Tranquil Pathway Business Card</title>
<link href="https://fonts.googleapis.com/css2?family=Lato:wght@400;700&family=Open+Sans:wght@400;600;700&display=swap" rel="stylesheet">
<style>
  :root {
    --navy: #1f2a63;
    --grey: #5f6062;
    --white: #ffffff;
    --ink: #1a1a1a;
    --backdrop: #e4e6e8;
  }
  * { box-sizing: border-box; margin: 0; padding: 0; }
  html, body { width: 1200px; height: 898px; overflow: hidden; background: var(--backdrop); }
  .canvas { position: relative; width: 1200px; height: 898px; }
  .card {
    position: absolute; width: 560px; height: 320px; overflow: hidden;
    box-shadow: 0 6px 18px rgba(0,0,0,.18);
  }
  /* Back of card */
  .card-back { left: 140px; top: 90px; background: var(--navy); color: var(--white); font-family: 'Lato', sans-serif; }
  .back-brand { position: absolute; left: 0; right: 0; top: 78px; display: flex; align-items: center; justify-content: center; gap: 18px; }
  .brand-circle { width: 84px; height: 84px; border-radius: 50%; border: 7px solid var(--white); flex: none; }
  .brand-divider { width: 2px; height: 92px; background: var(--white); }
  .brand-name { font-family: 'Open Sans', sans-serif; font-weight: 700; font-size: 30px; line-height: 1.05; text-transform: uppercase; letter-spacing: 1px; }
  .back-phone { position: absolute; left: 0; right: 0; top: 210px; text-align: center; font-size: 17px; letter-spacing: 1.5px; display: flex; justify-content: center; align-items: center; gap: 6px; }
  .back-web { position: absolute; left: 0; right: 0; top: 252px; text-align: center; font-size: 16px; letter-spacing: 1.5px; }
  /* Front of card */
  .card-front { left: 500px; top: 488px; background: var(--white); font-family: 'Open Sans', sans-serif; color: var(--ink); }
  .front-brand { position: absolute; left: 36px; top: 28px; display: flex; align-items: center; gap: 14px; }
  .front-brand .brand-circle { width: 76px; height: 76px; border: 7px solid var(--grey); background: var(--navy); }
  .front-brand .brand-divider { background: var(--grey); height: 80px; width: 1.5px; }
  .front-brand .brand-name { color: var(--navy); font-size: 26px; }
  .rule { position: absolute; left: 40px; right: 30px; top: 141px; height: 1.5px; background: var(--navy); }
  .person-name { position: absolute; left: 40px; top: 114px; font-size: 18px; line-height: 24px; color: var(--ink); }
  .person-role { position: absolute; left: 40px; top: 148px; font-size: 14px; line-height: 20px; color: var(--navy); }
  .address { position: absolute; right: 30px; top: 150px; text-align: right; font-size: 13.5px; line-height: 20px; color: var(--ink); font-style: normal; }
  .contacts { position: absolute; left: 40px; top: 196px; font-size: 14px; line-height: 24px; }
  .contacts li { list-style: none; display: flex; align-items: center; gap: 10px; }
  .swoosh { position: absolute; left: 0; bottom: 0; width: 560px; height: 70px; }
  .front-web { position: absolute; right: 28px; bottom: 10px; color: var(--white); font-size: 15px; line-height: 20px; }
</style>
</head>
<body>
<div class="canvas">
  <section class="card card-back" aria-label="Back of card">
    <div class="back-brand">
      <span class="brand-circle"></span>
      <span class="brand-divider"></span>
      <span class="brand-name">Tranquil<br>Pathway</span>
    </div>
    <p class="back-phone">
      <svg width="14" height="14" viewBox="0 0 24 24" aria-hidden="true"><path fill="#fff" d="M6.6 10.8a15 15 0 0 0 6.6 6.6l2.2-2.2c.3-.3.7-.4 1-.2 1.1.4 2.3.6 3.6.6.6 0 1 .4 1 1V20c0 .6-.4 1-1 1A17 17 0 0 1 3 4c0-.6.4-1 1-1h3.5c.6 0 1 .4 1 1 0 1.3.2 2.5.6 3.6.1.3 0 .7-.2 1z"/></svg>
      1300 958 471
    </p>
    <p class="back-web">www.TranquilPathway.example.au</p>
  </section>

  <section class="card card-front" aria-label="Front of card">
    <div class="front-brand">
      <span class="brand-circle"></span>
      <span class="brand-divider"></span>
      <span class="brand-name">Tranquil<br>Pathway</span>
    </div>
    <p class="person-name">Colin Marchetti</p>
    <div class="rule"></div>
    <p class="person-role">Professional Clinical Hypnotherapist</p>
    <address class="address">
      Consulting Rooms<br>(Near Lindqvist Hospital)<br>482 Brackenfield Road<br>Dunmore VIC 3987
    </address>
    <ul class="contacts">
      <li>
        <svg width="11" height="15" viewBox="0 0 11 15" aria-hidden="true"><rect x="1" y="0.5" width="9" height="14" rx="1.5" fill="none" stroke="#5f6062"/><rect x="2.5" y="2.5" width="6" height="5" fill="#5f6062"/></svg>
        0455 872 604
      </li>
      <li>
        <svg width="14" height="10" viewBox="0 0 14 10" aria-hidden="true"><rect x="0.5" y="0.5" width="13" height="9" fill="none" stroke="#1f2a63"/><path d="M0.5 0.5 7 6 13.5 0.5" fill="none" stroke="#1f2a63"/></svg>
        Colin@TranquilPathway.example.au
      </li>
    </ul>
    <svg class="swoosh" viewBox="0 0 560 90" preserveAspectRatio="none" aria-hidden="true">
      <path d="M0 90 C120 40 250 20 400 22 C300 30 160 60 60 90 Z" fill="#5f6062"/>
      <path d="M60 90 C200 52 330 40 560 20 L560 90 Z" fill="#1f2a63"/>
    </svg>
    <p class="front-web">www.TranquilPathway.example.au</p>
  </section>
</div>
</body>
</html>
```